Halvern Aviation Group - "Coming Soon" Main Company Webpage

Design a main webpage that can be posted while a fully functional website is constructed. The design should be created to convey a sense of luxury and exclusivity. The main page should contain only one photo as the background. The photo I believe to show "luxury" and "Exclusivity" is listed as "Global Luxury Photo". I have included two other photos as well to aid in providing a variety of presentations.
The "Member PQTR" logo should appear somewhere on the main page but be less prevalent than the main company logo. "Coming Soon" should also appear to convey that a website is being constructed.
Tabs for the website:
- Aircraft Management
- Aircraft Sales
- Pilot Services
- Charter
- Flight Training

```html
<!DOCTYPE html>
<html lang="en">
<head>
<meta charset="utf-8">
<title>Halvern Aviation Group – Coming Soon</title>
<link rel="stylesheet" href="https://fonts.googleapis.com/css2?family=Jost:wght@400;500&family=Playfair+Display:ital,wght@0,400;1,700&family=Michroma&display=swap">
<style>
  :root{
    --topbar:#5f9cd6;
    --topbar-text:#1857a8;
    --nav:#0b5cb2;
    --nav-line:#2a6fbd;
    --nav-text:#a9c7ea;
    --logo:#b7c6d8;
    --sky-top:#3c78bf;
    --sky-mid:#2c67b0;
    --sky-low:#1a55a2;
    --panel:#0a5cb3;
    --white:#ffffff;
    --ink:#000000;
    --ctrl-line:#8fb2dd;
  }
  *{margin:0;padding:0;box-sizing:border-box}
  html,body{width:1200px;height:610px;overflow:hidden}
  body{font-family:"Jost",sans-serif;position:relative;background:var(--sky-mid)}

  .hero-photo{position:absolute;inset:0;
    background:
      radial-gradient(ellipse 420px 220px at 1000px 330px, rgba(120,160,210,.45), transparent 70%),
      radial-gradient(ellipse 500px 200px at 220px 380px, rgba(90,140,205,.35), transparent 70%),
      linear-gradient(180deg,var(--sky-top) 0%,var(--sky-mid) 55%,var(--sky-low) 100%);}
  .hero-accent{position:absolute;left:290px;top:205px;width:175px;height:100px;border-radius:50%;
    background:radial-gradient(ellipse at center, rgba(230,238,248,.55), transparent 70%);}

  .top-bar{position:absolute;left:0;top:0;width:1200px;height:26px;background:var(--topbar);
    display:flex;justify-content:flex-end;align-items:center;padding-right:112px;
    font-size:10.5px;letter-spacing:.9px;color:var(--topbar-text);text-transform:uppercase}
  .top-bar .sep{margin:0 16px}

  .main-nav{position:absolute;left:0;top:26px;width:1200px;height:61px;background:var(--nav)}
  .brand{position:absolute;left:113px;top:17px;color:var(--logo);font-family:"Michroma",sans-serif;line-height:1}
  .brand-name{display:block;font-size:19px;letter-spacing:2px}
  .brand-sub{display:block;font-size:8.6px;letter-spacing:1.6px;margin-top:4px}
  .nav-list{position:absolute;left:475px;top:0;height:61px;display:flex;list-style:none;
    border-left:1px solid var(--nav-line)}
  .nav-list li{height:61px;display:flex;align-items:center;padding:0 13px;
    border-right:1px solid var(--nav-line);color:var(--nav-text);font-size:13px;letter-spacing:.1px;text-transform:uppercase}

  .announce{position:absolute;left:360px;top:205px;width:498px;height:200px;background:var(--panel);
    border:3px solid var(--white);text-align:center;color:var(--white)}
  .corner{position:absolute;width:26px;height:26px;border-color:var(--white);border-style:solid}
  .corner-tr{left:837px;top:200px;border-width:5px 5px 0 0}
  .corner-bl{left:352px;top:384px;border-width:0 0 5px 5px}
  .tag{position:absolute;left:202px;top:44px;width:75px;height:18px;background:var(--ink);
    font-size:12.5px;line-height:18px;letter-spacing:.3px}
  .tag::before{content:"";position:absolute;left:-12px;top:9px;width:18px;height:1px;background:var(--white)}
  .headline{position:absolute;left:0;right:0;top:60px;font-family:"Playfair Display",serif;
    font-weight:400;font-size:60px;line-height:1}
  .headline em{font-weight:700;font-style:italic}
  .subline{position:absolute;left:0;right:0;top:137px;font-size:20.5px;font-weight:400}

  .slider-ctrl{position:absolute;left:11px;top:559px;display:flex;border:1px solid var(--ctrl-line)}
  .slider-ctrl span{width:39px;height:38px;display:flex;align-items:center;justify-content:center}
  .slider-ctrl span+span{border-left:1px solid var(--ctrl-line)}

  .social-rail{position:absolute;left:1163px;top:487px;width:20px}
  .social-rail::before{content:"";display:block;width:1px;height:38px;background:var(--ctrl-line);margin:0 0 5px 10px}
  .social-rail span{display:block;width:20px;height:20px;border:1px solid var(--ctrl-line);margin-bottom:3px}

  .member-badge{position:absolute;left:1029px;top:556px;width:109px;height:38px;border-radius:4px;
    background:#6f93bf;border:1px solid #8eaed5;display:flex;align-items:center;justify-content:center;gap:6px;
    color:#1c3f72;font-size:11px;font-weight:500;letter-spacing:.4px}
  .member-badge i{width:10px;height:10px;border-radius:50%;background:#1c3f72}
</style>
</head>
<body>
  <div class="hero-photo" role="img" aria-label="Blue-toned photo of a private jet flying above clouds"></div>
  <div class="hero-accent" role="img" aria-label="Small illustration of an airliner with clouds"></div>

  <header>
    <div class="top-bar">
      <span>Phone : 555-010-4821</span><span class="sep">|</span>
      <span>Email: hello@halvernaviation.example</span><span class="sep">|</span>
      <span>About</span><span class="sep">|</span>
      <span>Contact</span>
    </div>
    <nav class="main-nav">
      <div class="brand"><span class="brand-name">HALVERN</span><span class="brand-sub">AVIATION GROUP</span></div>
      <ul class="nav-list">
        <li>Aircraft Management</li>
        <li>Aircraft Sales</li>
        <li>Pilot Services</li>
        <li>Charter</li>
        <li>Flight Training</li>
      </ul>
    </nav>
  </header>

  <div class="corner corner-tr"></div>
  <div class="corner corner-bl"></div>
  <section class="announce">
    <div class="tag">WE ARE</div>
    <h1 class="headline">Coming <em>Soon</em></h1>
    <p class="subline">Our Website is Under Construction</p>
  </section>

  <div class="slider-ctrl">
    <span><svg width="10" height="14" viewBox="0 0 10 14"><path d="M8 1 2 7l6 6" fill="none" stroke="#fff" stroke-width="1.5"/></svg></span>
    <span><svg width="10" height="14" viewBox="0 0 10 14"><path d="M2 1l6 6-6 6" fill="none" stroke="#fff" stroke-width="1.5"/></svg></span>
  </div>

  <div class="social-rail" aria-label="Social links"><span></span><span></span><span></span></div>

  <div class="member-badge"><i></i>Member PQTR</div>
</body>
</html>
```